Baby Shower Invite

Hello There, I would like to design the invitation for my baby boy shower,

It needs to be a template so I can add on the Message and Info

The theme is space, constellations, astral, astronomy, solar system, super nova, stars.
Please no Aliens or Rockets.

Here's what is should say:
Celestial shower of gifts and good wishes
Baby (Name) is on his way
Please join us on this astral event and mark it on your astronomy calendar

Sunday, Month ??? | at 2:00pm
Address
RSVP to (Name & Phone number)

Registered as (Names) at (Stores)

Thank you!!!

```html
<!DOCTYPE html>
<html lang="en">
<head>
<meta charset="UTF-8">
<title>Baby Shower Invitation – Capricorn</title>
<link rel="stylesheet" href="https://fonts.googleapis.com/css2?family=Questrial&family=Montserrat:wght@700&family=Allura&family=Yellowtail&display=swap">
<style>
  :root {
    --sky-core: #145468;
    --sky-mid: #1a3f68;
    --sky-edge: #142a55;
    --ink: #ffffff;
    --gold: #f4e41c;
    --glow: rgba(255, 255, 255, 0.9);
  }
  * { margin: 0; padding: 0; box-sizing: border-box; }
  html, body { width: 1019px; height: 1200px; overflow: hidden; }
  body { background: var(--sky-edge); }
  .invite {
    position: relative;
    width: 1019px;
    height: 1200px;
    overflow: hidden;
    color: var(--ink);
    font-family: "Questrial", "Helvetica Neue", Arial, sans-serif;
    background:
      radial-gradient(ellipse 75% 60% at 50% 18%, var(--sky-core) 0%, var(--sky-mid) 55%, var(--sky-edge) 100%);
  }
  .frame {
    position: absolute;
    left: 31px; top: 25px;
    width: 962px; height: 1138px;
    border: 3px solid var(--ink);
  }
  .starfield { position: absolute; inset: 0; width: 1019px; height: 1200px; }
  .sign-figure {
    position: absolute;
    left: 402px; top: 62px;
    width: 215px; height: 227px;
    border-radius: 40%;
    background: radial-gradient(circle at 50% 50%, rgba(255,255,255,0.95) 0%, rgba(235,245,250,0.75) 40%, rgba(255,255,255,0) 72%);
  }
  .line {
    position: absolute;
    left: 0; width: 1019px;
    text-align: center;
    line-height: 1;
    white-space: nowrap;
  }
  .sign-name { top: 314px; font-size: 42px; color: var(--gold); }
  .sign-dates { top: 364px; font-size: 21px; }
  .sign-traits { top: 409px; font-size: 41px; }
  .invite-lead { top: 516px; font-size: 17px; }
  .event-title { top: 556px; font-family: "Allura", cursive; font-size: 72px; }
  .event-tagline { top: 650px; font-size: 27px; }
  .baby-label { top: 694px; font-size: 32px; }
  .baby-name {
    top: 731px;
    font-family: "Montserrat", "Arial Black", sans-serif;
    font-weight: 700;
    font-size: 104px;
    letter-spacing: 2px;
  }
  .arrival-row {
    position: absolute;
    left: 104px; top: 838px;
    width: 808px; height: 28px;
    display: flex; align-items: center; gap: 12px;
    font-size: 25px;
  }
  .arrival-row .dots {
    flex: 1;
    height: 5px;
    background-image: radial-gradient(circle, var(--ink) 2px, transparent 2.4px);
    background-size: 8px 5px;
    background-repeat: repeat-x;
  }
  .details { font-size: 27px; }
  .field {
    position: absolute;
    display: flex; align-items: flex-end;
    line-height: 1;
    white-space: nowrap;
  }
  .blank {
    display: inline-block;
    border-bottom: 2px solid var(--ink);
    height: 24px;
    margin: 0 10px;
  }
  .field-date { left: 183px; top: 893px; }
  .field-address { left: 104px; top: 927px; }
  .field-rsvp { left: 199px; top: 960px; }
  .field-registry { left: 138px; top: 994px; }
  .closing {
    top: 1070px;
    font-family: "Yellowtail", cursive;
    font-size: 27px;
  }
</style>
</head>
<body>
<main class="invite">
  <svg class="starfield" viewBox="0 0 1019 1200" aria-hidden="true">
    <g fill="#ffffff">
      <circle cx="61" cy="160" r="4"/>
      <circle cx="58" cy="325" r="3"/>
      <circle cx="365" cy="199" r="4"/>
      <circle cx="910" cy="277" r="3.5"/>
      <circle cx="474" cy="360" r="3.5"/>
      <circle cx="631" cy="494" r="3"/>
      <circle cx="944" cy="626" r="4"/>
      <circle cx="67" cy="876" r="3.5"/>
      <circle cx="950" cy="917" r="3"/>
      <circle cx="304" cy="766" r="3.5"/>
      <circle cx="711" cy="767" r="3"/>
      <circle cx="785" cy="672" r="3"/>
    </g>
    <g fill="#ffffff">
      <path d="M848 70 l2 6 6 2 -6 2 -2 6 -2 -6 -6 -2 6 -2z"/>
      <path d="M164 217 l2 6 6 2 -6 2 -2 6 -2 -6 -6 -2 6 -2z"/>
      <path d="M765 362 l2 6 6 2 -6 2 -2 6 -2 -6 -6 -2 6 -2z"/>
      <path d="M124 641 l2 6 6 2 -6 2 -2 6 -2 -6 -6 -2 6 -2z"/>
    </g>
  </svg>

  <div class="frame"></div>

  <div class="sign-figure" role="img" aria-label="Glowing white Capricorn goat silhouette with curled horn"></div>

  <p class="line sign-name">CAPRICORN</p>
  <p class="line sign-dates">DECEMBER 22 – JANUARY 19</p>
  <p class="line sign-traits">WISE, INDEPENDENT, LOYAL</p>

  <p class="line invite-lead">YOU’RE INVITED TO AN ASTRAL OCCURENCE</p>
  <h1 class="line event-title" style="font-weight:400">Baby Shower</h1>
  <p class="line event-tagline">CELESTIAL SHOWER OF GIFTS AND GOOD WISHES</p>
  <p class="line baby-label">BABY</p>
  <h2 class="line baby-name">LOREM IPSUM</h2>

  <div class="arrival-row">
    <span class="dots"></span>
    <span>IS ON HIS WAY</span>
    <span class="dots"></span>
  </div>

  <div class="details">
    <p class="field field-date">SUNDAY,<span class="blank" style="width:346px"></span>AT 2:00 PM</p>
    <p class="field field-address">ADDRESS<span class="blank" style="width:670px;margin-right:0"></span></p>
    <p class="field field-rsvp">RSVP TO<span class="blank" style="width:486px;margin-right:0"></span></p>
    <p class="field field-registry">REGISTERED AS<span class="blank" style="width:240px;margin-right:2px"></span>, AT<span class="blank" style="width:202px;margin-right:0"></span></p>
  </div>

  <p class="line closing">Please join us on this astral event and mark it on your astronomy calendar!</p>
</main>
</body>
</html>
```